Bref créative
Quillmont Care Associates
Business Cards & Stationary
Bright & Fun-filled
Harold J. Mabbery, Ph.D.
Co-founder
4815 North Larkin Road
Vista, CA 92083
drhmabbery@examplemail.net
Licensed Psychologist PSY58706
On the front of the card, we would like to see some versions with the logos symbol.
This business card is for a California Board Licensed Psychologist.
The look of this should be professional, but because it is for therapy, we would like it to be professional with a hint of:
* warm and welcoming
* serenity, tranquility and happiness
* positive, future, growth
On the back of the business card please place the:
1. Logo symbol and company name
2. Child, Adolescence, Family, Adult Therapy
logo
We need to see how the back of a card looks with the Quillmont Care Logo and the following information attached.

```html
<!DOCTYPE html>
<html lang="en">
<head>
<meta charset="utf-8">
<title>Quillmont Care Associates — Stationery Set</title>
<link href="https://fonts.googleapis.com/css2?family=Lato:wght@400;700&display=swap" rel="stylesheet">
<style>
:root{
  --bg:#eceef0;
  --paper:#ffffff;
  --blue:#1b8fd8;
  --blue-light:#5fbdee;
  --teal-soft:#c4e9f0;
  --ink:#2a6f9e;
  --grey:#7d8790;
  --faint:#e4f2fa;
}
*{margin:0;padding:0;box-sizing:border-box}
html,body{width:1200px;height:437px;overflow:hidden;background:var(--bg);font-family:"Lato",sans-serif}
.canvas{position:relative;width:1200px;height:437px}
.piece{position:absolute;background:var(--paper);box-shadow:0 1px 4px rgba(0,0,0,.18);overflow:hidden}
.caption{position:absolute;font-size:7px;color:var(--grey);text-align:center}
.brand{display:flex;align-items:center;gap:4px;color:var(--blue);font-weight:700;letter-spacing:.5px;white-space:nowrap}
.brand .dot{border-radius:50%;background:var(--blue);flex:none}
.brand small{display:block;font-weight:400;font-size:.5em;letter-spacing:.2px}
.info{color:var(--ink);font-size:4.5px;line-height:1.5;white-space:nowrap}
.halo{position:absolute;border-radius:50%;border:10px solid var(--faint)}
svg{position:absolute;display:block}
/* business cards */
.card{left:10px;width:110px;height:64px}
.card-front{top:67px}
.card-front .info{position:absolute;right:6px;top:5px;text-align:right;font-size:4px}
.card-front .brand{position:absolute;left:6px;top:45px;font-size:7px}
.card-front .brand .dot{width:9px;height:9px}
.card-back{top:196px}
.card-back .brand{position:absolute;left:8px;top:22px;font-size:8px}
.card-back .brand .dot{width:10px;height:10px}
.card-back .info{position:absolute;left:8px;top:40px}
.card-blue{top:312px;background:var(--blue)}
.card-blue .brand{position:absolute;left:8px;top:24px;font-size:8px;color:#fff}
.card-blue .brand .dot{width:10px;height:10px;background:#fff}
/* letterheads */
.letter{top:19px;width:271px;height:389px}
.letter-one{left:204px}
.letter-two{left:516px}
.letter .brand{position:absolute;left:16px;top:22px;font-size:9px}
.letter .brand .dot{width:12px;height:12px}
.letter .info{position:absolute;left:140px;top:20px}
.letter .footer{position:absolute;left:40px;right:40px;bottom:14px;text-align:center;font-size:4px;color:var(--grey)}
/* envelopes */
.env{left:900px;width:288px}
.env .brand{position:absolute;font-size:7px}
.env .brand .dot{width:9px;height:9px}
.env .info{position:absolute}
</style>
</head>
<body>
<div class="canvas">

  <!-- business cards -->
  <div class="piece card card-front">
    <div class="info">Harold J. Mabbery, Ph.D.<br>Co-founder<br>4815 North Larkin Road<br>Vista, CA 92083<br>drhmabbery@examplemail.net<br>Licensed Psychologist PSY58706</div>
    <div class="brand"><span class="dot"></span><span>QUILLMONT CARE<small>Child · Adolescent · Family · Adult Therapy</small></span></div>
  </div>
  <div class="caption" style="left:10px;top:174px;width:110px">Front Card</div>

  <div class="piece card card-back">
    <div class="halo" style="width:60px;height:60px;right:-26px;top:-4px"></div>
    <div class="brand"><span class="dot"></span><span>QUILLMONT CARE<small>Quillmont Care Associates</small></span></div>
    <div class="info">Child, Adolescence, Family, Adult Therapy</div>
  </div>
  <div class="caption" style="left:10px;top:292px;width:110px">Back Card Option 01</div>

  <div class="piece card card-blue">
    <div class="brand"><span class="dot"></span><span>QUILLMONT CARE<small>Child, Adolescence, Family, Adult Therapy</small></span></div>
  </div>
  <div class="caption" style="left:10px;top:409px;width:110px">Back Card Option 02</div>

  <!-- letterhead option 01 -->
  <div class="piece letter letter-one">
    <svg width="271" height="389" viewBox="0 0 271 389">
      <path d="M205 0 H271 V70 Q262 20 205 0Z" fill="var(--blue)"/>
      <path d="M225 0 H271 V40 Q262 10 225 0Z" fill="var(--blue-light)"/>
      <path d="M0 340 Q70 370 140 389 H0Z" fill="var(--blue-light)"/>
      <path d="M0 355 Q50 378 100 389 H0Z" fill="var(--blue)"/>
    </svg>
    <div class="halo" style="width:150px;height:150px;left:60px;top:110px;border-width:18px"></div>
    <div class="brand"><span class="dot"></span><span>QUILLMONT CARE<small>Child · Adolescent · Family · Adult Therapy</small></span></div>
    <div class="info">Harold J. Mabbery, Ph.D.<br>4815 North Larkin Road<br>Vista, CA 92083<br>(760) 555-0142<br>drhmabbery@examplemail.net</div>
  </div>
  <div class="caption" style="left:204px;top:414px;width:271px">Letterhead option 01</div>

  <!-- letterhead option 02 -->
  <div class="piece letter letter-two">
    <svg width="271" height="389" viewBox="0 0 271 389">
      <path d="M271 290 Q240 360 170 389 H271Z" fill="var(--blue-light)"/>
      <path d="M271 330 Q250 370 210 389 H271Z" fill="var(--blue)"/>
    </svg>
    <div class="halo" style="width:150px;height:150px;left:60px;top:110px;border-width:18px"></div>
    <div class="brand"><span class="dot"></span><span>QUILLMONT CARE<small>Child · Adolescent · Family · Adult Therapy</small></span></div>
    <div class="footer">4815 North Larkin Road, Vista, CA 92083 · (760) 555-0142 · drhmabbery@examplemail.net<br>www.quillmontcare.net</div>
  </div>
  <div class="caption" style="left:516px;top:414px;width:271px">Letterhead option 02</div>

  <!-- envelopes -->
  <div class="piece env" style="top:34px;height:100px;background:var(--teal-soft)">
    <svg width="288" height="100" viewBox="0 0 288 100"><path d="M0 0 L144 62 L288 0Z" fill="#dff3f6"/></svg>
    <div class="brand" style="left:128px;top:44px"><span class="dot"></span></div>
  </div>
  <div class="piece env" style="top:138px;height:90px">
    <svg width="288" height="90" viewBox="0 0 288 90"><path d="M0 0 L144 52 L288 0Z" fill="var(--blue)"/><path d="M0 0 L144 40 L288 0Z" fill="var(--blue-light)"/></svg>
    <div class="brand" style="left:138px;top:18px;color:#fff"><span class="dot" style="background:#fff"></span></div>
  </div>
  <div class="piece env" style="top:234px;height:74px">
    <svg width="288" height="74" viewBox="0 0 288 74"><path d="M0 0 L144 40 L288 0Z" fill="#f4f6f8" stroke="#dfe3e6"/></svg>
  </div>
  <div class="piece env" style="top:312px;height:96px">
    <svg width="288" height="96" viewBox="0 0 288 96"><path d="M250 0 Q232 48 250 96 H288 V0Z" fill="var(--blue)"/><path d="M262 0 Q248 48 262 96 H288 V0Z" fill="var(--blue-light)"/></svg>
    <div class="halo" style="width:60px;height:60px;left:-16px;top:40px;border-width:8px"></div>
    <div class="brand" style="left:12px;top:12px"><span class="dot"></span><span>QUILLMONT CARE</span></div>
    <div class="info" style="left:12px;top:26px">4815 North Larkin Road<br>Vista, CA 92083</div>
  </div>
  <div class="caption" style="left:900px;top:414px;width:288px">Envelope Front &amp; Back</div>

</div>
</body>
</html>
```